Coral Bay Villa Offer

I need a flyer that i can use at different venues that offers the same thing - a complimentary stay in the Linden Feast company owned Coral Bay Villa for 4 nights and 5 days. I need a template of a design that i can modify so it's venue specific. For example, i want it to say: "Confirm your reservation at XXXXXXX venue alongside the Linden Feast and receive a complimentary stay in the Linden Feast's company owned villa for 4 nights and 5 days! Daily cleaning, shopping and cooking is included."

Target Market(s)

Wedding Clients for our catering company at different off site wedding venues.

Industry/Entity Type

Wedding

Font styles to use
Serif

Colors

Designer to choose colors to be used in the design.

Requirements
Must have
• Linden Feast Logo
• Stylized Photos of the condo and puerto vallarta in general
Nice to have
• The Linden Feast is the Highest Rated Caterer in California on RAVO
• The Linden Feast offers turn key discounted all inclusive wedding vendor packages

```html
<!DOCTYPE html>
<html lang="en">
<head>
<meta charset="utf-8">
<title>Coral Bay Villa Offer — The Linden Feast</title>
<link rel="stylesheet" href="https://fonts.googleapis.com/css2?family=Cinzel:wght@400;600;700&family=Arimo:ital,wght@0,400;0,700;1,400&display=swap">
<style>
  :root {
    --stage-top: #ffffff;
    --stage-bottom: #e2e2e2;
    --navy: #18202e;
    --navy-deep: #121926;
    --gold-light: #f3c54a;
    --gold-mid: #d99a1f;
    --gold-dark: #a8701a;
    --accent-yellow: #f4c842;
    --white: #ffffff;
    --soft-white: #eef1f5;
    --badge-blue: #1e8fd8;
    --badge-red: #d32323;
    --badge-cream: #fbf4dc;
    --badge-sky: #6cc4ef;
  }
  * { margin: 0; padding: 0; box-sizing: border-box; }
  html, body { width: 1200px; height: 1000px; overflow: hidden; }
  body {
    position: relative;
    background: linear-gradient(180deg, var(--stage-top) 0%, var(--stage-bottom) 100%);
    font-family: "Arimo", Arial, sans-serif;
  }
  .flyer {
    position: absolute;
    left: 243px; top: 17px;
    width: 748px; height: 966px;
    background: var(--navy);
    overflow: hidden;
  }
  .hero-photo {
    position: absolute; left: 0; top: 0;
    width: 748px; height: 500px;
    background:
      linear-gradient(180deg, rgba(18,25,38,0.55) 0%, rgba(18,25,38,0.15) 35%, rgba(18,25,38,0.1) 70%, var(--navy) 100%),
      radial-gradient(ellipse at 55% 85%, #1f5e9c 0%, rgba(31,94,156,0) 40%),
      linear-gradient(100deg, #2c4a34 0%, #5b6a5c 30%, #8c8f8a 55%, #4d6446 80%, #2a3e2d 100%);
  }
  .frame { position: absolute; background: linear-gradient(90deg, var(--gold-dark), var(--gold-light), var(--gold-mid)); }
  .frame.v { width: 4px; background: linear-gradient(180deg, var(--gold-light), var(--gold-mid), var(--gold-dark), var(--gold-light)); }
  .frame.h { height: 4px; }

  .brand { position: absolute; left: 160px; top: 36px; display: flex; align-items: flex-start; gap: 22px; }
  .brand-mark { width: 62px; height: 62px; background: var(--white); margin-top: 16px; }
  .brand-name {
    font-family: "Cinzel", Georgia, serif; font-weight: 400;
    font-size: 36px; color: var(--white); letter-spacing: 1px; line-height: 44px;
  }
  .brand-tag {
    font-family: "Cinzel", Georgia, serif; font-size: 16px;
    letter-spacing: 7px; color: var(--white); line-height: 21px; margin-top: 6px;
  }

  .headline {
    position: absolute; left: 0; top: 230px; width: 748px;
    text-align: center; color: var(--white);
    font-family: "Cinzel", Georgia, serif; font-size: 34px; line-height: 44px;
    text-shadow: 0 2px 6px rgba(0,0,0,0.55);
  }
  .headline .lead { font-weight: 700; }

  .gallery { position: absolute; left: 55px; top: 468px; width: 636px; height: 137px; display: flex; }
  .gallery .shot { flex: 1; height: 100%; }
  .shot.terrace { background: linear-gradient(160deg, #c9c4b6, #7a4a3a 60%, #5a2a22); }
  .shot.lounge { background: linear-gradient(160deg, #e6e1da, #a4352a 55%, #4a3a36); }
  .shot.bedroom { background: linear-gradient(160deg, #c2a27a, #2b2a30 50%, #5d7ea8); }
  .shot.spa { background: linear-gradient(160deg, #6e9a5a, #bfe3ee 50%, #7ec0dc); }

  .rule { position: absolute; left: 129px; width: 502px; height: 3px; background: linear-gradient(90deg, var(--gold-dark), var(--gold-light), var(--gold-mid)); }

  .offer { position: absolute; left: 0; width: 748px; text-align: center; color: var(--white); }
  .offer-lead { top: 636px; color: var(--accent-yellow); font-size: 19px; }
  .venue-name { top: 659px; font-size: 27px; font-weight: 700; }
  .offer-partner { top: 692px; font-size: 19px; color: var(--soft-white); }
  .offer-perks { top: 734px; font-size: 19px; }
  .offer-note { top: 782px; font-size: 14px; font-style: italic; color: var(--soft-white); }

  .badges { position: absolute; left: 0; top: 830px; width: 748px; height: 70px; }
  .badge { position: absolute; }
  .badge.listing { left: 105px; top: 10px; width: 105px; height: 46px; background: var(--badge-blue); clip-path: polygon(0 100%, 30% 0, 100% 0, 100% 100%); }
  .badge.rating { left: 240px; top: 22px; width: 117px; height: 30px; background: var(--badge-red); }
  .badge.award { left: 410px; top: 0; width: 66px; height: 68px; background: var(--badge-cream); border: 3px solid var(--gold-mid); }
  .badge.love { left: 524px; top: 8px; width: 119px; height: 38px; background: var(--badge-sky); border-radius: 4px; }

  .website {
    position: absolute; left: 0; top: 922px; width: 748px; text-align: center;
    font-family: "Cinzel", Georgia, serif; font-size: 14px; letter-spacing: 1.5px; color: var(--white);
  }
</style>
</head>
<body>
  <main class="flyer">
    <div class="hero-photo" role="img" aria-label="Coral Bay Villa building with tropical gardens and a curved blue swimming pool"></div>

    <div class="frame v" style="left:32px; top:83px; height:850px;"></div>
    <div class="frame v" style="left:713px; top:83px; height:850px;"></div>
    <div class="frame h" style="left:32px; top:83px; width:143px;"></div>
    <div class="frame h" style="left:575px; top:83px; width:142px;"></div>
    <div class="frame h" style="left:32px; top:929px; width:205px;"></div>
    <div class="frame h" style="left:509px; top:929px; width:208px;"></div>

    <header class="brand">
      <div class="brand-mark"></div>
      <div>
        <div class="brand-name">THE LINDEN FEAST</div>
        <div class="brand-tag">CATERING &amp;<br>EVENT DESIGN</div>
      </div>
    </header>

    <h1 class="headline">
      <span class="lead">RECEIVE A COMPLIMENTARY</span><br>
      STAY IN THE LINDEN FEAST’S<br>
      COMPANY OWNED VILLA FOR<br>
      4 NIGHTS AND 5 DAYS!
    </h1>

    <section class="gallery">
      <div class="shot terrace" role="img" aria-label="Villa terrace with dining table and ocean view"></div>
      <div class="shot lounge" role="img" aria-label="Villa living room with red accent wall and leather sofa"></div>
      <div class="shot bedroom" role="img" aria-label="Villa bedroom with dark headboard and blue bedding"></div>
      <div class="shot spa" role="img" aria-label="Outdoor hot tub surrounded by garden plants"></div>
    </section>

    <div class="rule" style="top:622px;"></div>
    <p class="offer offer-lead">WHEN YOU CONFIRM YOUR RESERVATION AT</p>
    <p class="offer venue-name">THE VENUE NAME</p>
    <p class="offer offer-partner">ALONGSIDE THE LINDEN FEAST</p>
    <div class="rule" style="top:722px;"></div>
    <p class="offer offer-perks">Daily cleaning, shopping and cooking is included.</p>
    <p class="offer offer-note">The Linden Feast offers turn key discounted all inclusive wedding vendor packages</p>

    <div class="badges">
      <div class="badge listing"></div>
      <div class="badge rating"></div>
      <div class="badge award"></div>
      <div class="badge love"></div>
    </div>

    <p class="website">WWW.THELINDENFEAST.COM</p>
  </main>
</body>
</html>
```